DM - management consultant

Business card - contemporary design

Front info
Dorian Maples

(Address not necessary)
PO Box 7386
Belmont, CA 94002

(650) 555-0143
dm@dorianmapl.es

Chirpline: dmq527
Folkbook: /Dorian.Maples
Linkwork: /in/dorianmaples

Back or Front
www.dorianmaples.net
Facilitation & coaching, change management, strategic partnerships, business improvement

Target Market(s)

High tech businesses - mostly startups in Silicon Valley

Industry/Entity Type

Business

Font styles to use
Sans Serif

Colors

Designer to choose colors to be used in the design.

```html
<!DOCTYPE html>
<html lang="en">
<head>
<meta charset="utf-8">
<title>Dorian Maples – Business Card</title>
<link rel="stylesheet" href="https://fonts.googleapis.com/css2?family=Roboto:wght@400;500&family=Oswald:wght@300&family=Cormorant+SC:wght@500&display=swap">
<style>
  :root{
    --page:#e9e7e3;
    --ink-black:#151515;
    --ink-charcoal:#2a2a2a;
    --paper-light:#f4f4f4;
    --paper-mid:#d6d6d6;
    --band-grey:#b4b4b4;
    --text-dark:#3a3a3a;
    --text-white:#ffffff;
    --brand-green:#7cc242;
    --social-blue:#2aa9e0;
    --social-navy:#3b5a9a;
    --social-teal:#2e8a3a;
  }
  *{box-sizing:border-box;margin:0;padding:0}
  html,body{width:1200px;height:900px;overflow:hidden;background:var(--page)}
  .sheet{position:relative;width:1200px;height:900px}
  .card{position:absolute;top:290px;width:560px;height:320px;overflow:hidden;box-shadow:0 6px 18px rgba(0,0,0,.18)}
  .card--back{left:27px;background:radial-gradient(ellipse at 50% 40%,var(--ink-charcoal),var(--ink-black) 75%);color:var(--text-white);font-family:"Roboto",sans-serif;text-align:center}
  .card--front{left:613px;background:linear-gradient(180deg,var(--paper-light) 0%,#e2e2e2 45%,var(--paper-mid) 100%);font-family:"Roboto",sans-serif;color:var(--text-dark)}

  .brand-mark{display:inline-flex;align-items:center;gap:10px;font-family:"Roboto",sans-serif;font-weight:500;color:var(--brand-green)}
  .brand-mark__square{display:inline-block;background:var(--brand-green);border-radius:4px}
  .card--back .brand-mark{margin-top:44px;font-size:64px;line-height:1}
  .card--back .brand-mark__square{width:26px;height:26px}
  .role{margin-top:22px;font-size:19px;letter-spacing:.32em;text-transform:uppercase}
  .web{margin-top:14px;font-size:19px;letter-spacing:.06em}
  .services{margin-top:22px;font-size:14.5px;line-height:1.25;letter-spacing:.05em}

  .card--front .brand-mark{position:absolute;top:30px;right:62px;font-size:48px;line-height:1}
  .card--front .brand-mark__square{width:20px;height:20px}
  .address-band{position:absolute;left:0;right:0;top:128px;height:40px;background:linear-gradient(180deg,#c2c2c2,var(--band-grey))}
  .footer-strip{position:absolute;left:0;right:0;bottom:0;height:62px;background:linear-gradient(180deg,#c9c9c9,#e3e3e3)}
  .name-plate{position:absolute;left:0;top:150px;width:232px;height:104px;background:linear-gradient(160deg,var(--ink-charcoal),var(--ink-black));display:flex;align-items:flex-end;padding:0 0 22px 20px;box-shadow:2px 2px 6px rgba(0,0,0,.3)}
  .name-plate__name{font-family:"Cormorant SC",serif;font-weight:500;font-size:27px;letter-spacing:.06em;color:var(--text-white);white-space:nowrap}

  .contact{position:absolute;left:248px;top:135px;list-style:none;font-size:16px;letter-spacing:.05em}
  .contact li{display:flex;align-items:center;gap:10px;height:26px;white-space:nowrap}
  .contact svg{width:16px;height:16px;flex:none}

  .social{list-style:none;font-family:"Oswald",sans-serif;font-weight:300;font-size:19px;color:var(--text-dark)}
  .social__item{display:flex;align-items:center;gap:8px;position:absolute;height:26px;white-space:nowrap}
  .social__dot{width:22px;height:22px;border-radius:50%;flex:none}
  .social__item--link{left:318px;top:222px;font-size:18px}
  .social__item--link .social__dot{background:var(--social-teal)}
  .social__item--folk{left:248px;top:270px}
  .social__item--folk .social__dot{background:var(--social-navy)}
  .social__item--chirp{left:22px;top:276px}
  .social__item--chirp .social__dot{background:var(--social-blue)}
</style>
</head>
<body>
<main class="sheet">
  <section class="card card--back" aria-label="Card back">
    <div class="brand-mark"><span class="brand-mark__square"></span>DM</div>
    <p class="role">Management Consultant</p>
    <p class="web">www.dorianmaples.net</p>
    <p class="services">Facilitation &amp; coaching, change management,<br>strategic partnerships, business improvement</p>
  </section>

  <section class="card card--front" aria-label="Card front">
    <div class="brand-mark"><span class="brand-mark__square"></span>DM</div>
    <div class="address-band"></div>
    <div class="footer-strip"></div>
    <div class="name-plate"><span class="name-plate__name">Dorian Maples</span></div>
    <ul class="contact">
      <li>
        <svg viewBox="0 0 16 16" aria-hidden="true"><path fill="#222" d="M5 1h6v3h2v11H3V4h2zM6 6v2h1V6zm3 0v2h1V6zM6 10v2h1v-2zm3 0v2h1v-2z"/></svg>
        PO Box 7386 Belmont, CA 94002
      </li>
      <li>
        <svg viewBox="0 0 16 16" aria-hidden="true"><rect x="2.5" y="2.5" width="11" height="11" fill="none" stroke="#222" stroke-width="1.6"/></svg>
        (650) 555-0143
      </li>
      <li>
        <svg viewBox="0 0 16 16" aria-hidden="true"><rect x="1.5" y="2" width="13" height="9" fill="none" stroke="#222" stroke-width="1.5"/><path d="M5 14h6M8 11v3" stroke="#222" stroke-width="1.5"/></svg>
        dm@dorianmapl.es
      </li>
    </ul>
    <ul class="social">
      <li class="social__item social__item--link"><span class="social__dot"></span>Linkwork: /in/dorianmaples</li>
      <li class="social__item social__item--folk"><span class="social__dot"></span>Folkbook: /Dorian.Maples</li>
      <li class="social__item social__item--chirp"><span class="social__dot"></span>Chirpline: dmq527</li>
    </ul>
  </section>
</main>
</body>
</html>
```